Business Card Design for Orthopaedic Surgeon

This is a double-sided glossy business card. I prefer baby blue, teal, and green as color schemes. I have my logo already (many colors that you can choose from). I have photos and examples of my old card (very bland but has the information in it). I also have one that my assistant tried to design, but the writing is too small and I don't love the formatting. But it is close!
I would like my logo to be on the business card but I'm uploading my logo in many different colors so you can choose which one looks best based on the color scheme. I also uploaded many sized headshots so you can choose the best resolution one.

Additional information:
Correct business address:
4382 SE 58th Lane, Suite 305
Tamarac, FL 33347

Everything else on both business cards are accurate.

I actually need 2 different business cards generated. One that includes my cell phone number-- Personal cell: 585-614-3908 in addition to Office phone: (954) 362-5804 and Office Fax: 954-362-5819. Again, one card would have my personal cell and one wouldn't

Overall I just think the baby blue card (uploaded) is missing something on the front--of course it is also missing my office phone/fax/personal cell. I do want my website on the front too. Email: info@rkellowsurg.com

You can use your discretion about what goes on the front vs. what goes on the back to eliminated clutter.

Oh and on the back, I would like to list "Conditions Treated" (not specialties include). The list is:
Carpal Tunnel
Trigger Finger
Ganglion Cysts
Hand Tumors
Han & Wrist Arthritis
Hand, Wrist & Elbow Tendonitis
Fractures of the Hand, Wrist, Elbow and Humerus
Nerve Injuries of the Hand, Wrist & Elbow
Microsurgery
Wrist Arthroscopy
Endoscopic Surgery

Target Market(s)

Primary care doctors, Lawyers, patients

Industry/Entity Type

Medical

Contact Information for Business Card

Please see above in project description

Colors

Requirements
Must have
• -Correct office info, Board Certified Orthopaedic Hand & Upper Extremity Surgeon
Nice to have
• Something that is classy and wow!

```html
<!DOCTYPE html>
<html lang="en">
<head>
<meta charset="UTF-8">
<title>Renee Kellow, M.D – Business Card</title>
<link href="https://fonts.googleapis.com/css2?family=Montserrat:wght@400;500;600&display=swap" rel="stylesheet">
<style>
  :root {
    --backdrop: #d9e4e6;
    --card: #0d3a42;
    --baby-blue: #9fd6ee;
    --teal: #2a8c95;
    --green: #7ccaa0;
    --text: #f2f7f8;
    --photo-top: #e6eff2;
    --photo-bottom: #3d5a60;
  }
  * { margin: 0; padding: 0; box-sizing: border-box; }
  html, body { width: 900px; height: 1200px; overflow: hidden; }
  body {
    background: var(--backdrop);
    font-family: "Montserrat", Arial, sans-serif;
    color: var(--text);
    position: relative;
  }
  .card {
    position: absolute;
    left: 78px;
    width: 744px;
    background: var(--card);
    border-radius: 28px;
    overflow: hidden;
  }
  .card-front { top: 130px; height: 442px; }
  .card-back { top: 638px; height: 440px; }
  .card::after {
    content: "";
    position: absolute;
    left: 0; right: 0; bottom: 0;
    height: 6px;
    background: linear-gradient(90deg, var(--baby-blue), var(--teal), var(--green));
  }

  .headshot {
    position: absolute;
    left: 38px; top: 36px;
    width: 128px; height: 199px;
    border: 2px solid var(--baby-blue);
    background: linear-gradient(180deg, var(--photo-top) 0%, #8fa9ae 45%, var(--photo-bottom) 100%);
  }

  .brand {
    position: absolute;
    display: flex;
    align-items: center;
    gap: 10px;
    color: var(--baby-blue);
    font-weight: 500;
    white-space: nowrap;
  }
  .brand-dot {
    border: 2px solid var(--baby-blue);
    border-radius: 50%;
  }
  .card-front .brand { right: 40px; top: 88px; font-size: 22px; }
  .card-front .brand-dot { width: 22px; height: 22px; }
  .card-back .brand { right: 38px; top: 200px; font-size: 22px; }
  .card-back .brand-dot { width: 24px; height: 24px; }

  .identity {
    position: absolute;
    right: 37px; top: 198px;
    text-align: right;
  }
  .doctor-name {
    color: var(--baby-blue);
    font-size: 27px;
    font-weight: 600;
    letter-spacing: 0.5px;
    line-height: 36px;
    margin-bottom: 4px;
  }
  .credential { font-size: 18px; line-height: 29px; }
  .address { font-size: 18px; line-height: 29px; margin-top: 26px; }

  .contacts {
    position: absolute;
    left: 38px; top: 261px;
    list-style: none;
  }
  .contacts li {
    display: flex;
    align-items: center;
    height: 29px;
    font-size: 18px;
  }
  .contacts svg {
    width: 17px; height: 17px;
    margin-right: 10px;
    fill: var(--green);
  }

  .conditions-title {
    position: absolute;
    left: 28px; top: 30px;
    font-size: 20px;
    font-weight: 600;
    letter-spacing: 1px;
    color: var(--baby-blue);
    text-transform: uppercase;
  }
  .conditions {
    position: absolute;
    left: 28px; top: 72px;
    list-style: none;
  }
  .conditions li {
    font-size: 19px;
    line-height: 29.1px;
    display: flex;
    align-items: center;
  }
  .conditions li::before {
    content: "";
    width: 8px; height: 8px;
    border-radius: 50%;
    background: var(--green);
    margin-right: 6px;
  }
</style>
</head>
<body>

<section class="card card-front">
  <div class="headshot" role="img" aria-label="Headshot of the surgeon in a dark blazer"></div>

  <div class="brand"><span class="brand-dot"></span>Kellow Hand</div>

  <div class="identity">
    <h1 class="doctor-name">RENEE KELLOW, M.D</h1>
    <p class="credential">Board Certified</p>
    <p class="credential">Orthopaedic Hand &amp; Upper</p>
    <p class="credential">Extremity Surgeon</p>
    <p class="address">4382 SE 58th Lane,<br>Suite 305 Tamarac, FL 33347</p>
  </div>

  <ul class="contacts">
    <li>
      <svg viewBox="0 0 16 16" aria-hidden="true"><path d="M4.5 0h7A1.5 1.5 0 0 1 13 1.5v13a1.5 1.5 0 0 1-1.5 1.5h-7A1.5 1.5 0 0 1 3 14.5v-13A1.5 1.5 0 0 1 4.5 0zm.2 2v10.5h6.6V2zM8 13.3a.8.8 0 1 0 0 1.6.8.8 0 0 0 0-1.6z"/></svg>
      585-614-3908
    </li>
    <li>
      <svg viewBox="0 0 16 16" aria-hidden="true"><path d="M1 5c0-2 3-3 7-3s7 1 7 3v1.5h-3.5V5h-7v1.5H1zM4 7h8l2 4v3H2v-3zm4 1.5a2 2 0 1 0 0 4 2 2 0 0 0 0-4z"/></svg>
      (954) 362-5804
    </li>
    <li>
      <svg viewBox="0 0 16 16" aria-hidden="true"><path d="M4 1h8v4H4zM1 6h14v6h-2.5v-2h-9v2H1zM4.5 11h7v4h-7z"/></svg>
      954-362-5819
    </li>
    <li>
      <svg viewBox="0 0 16 16" aria-hidden="true"><path d="M1 4h14v1l-7 4.5L1 5zm0 2.3 7 4.5 7-4.5V12H1z"/></svg>
      info@rkellowsurg.com
    </li>
    <li>
      <svg viewBox="0 0 16 16" aria-hidden="true"><path d="M8 1a7 7 0 1 0 0 14A7 7 0 0 0 8 1zm-1 2.5c-.5 1-1.8 1.2-2 2.3-.2 1 1.2 1.4 2 1.2.9-.2 1.6.8 1.2 1.6-.5 1-.2 2.3.5 3.4-3-.2-5-2.6-5-5.5 0-1.3.5-2.5 1.2-3.4zm3 .1c1.6.9 2.6 2.5 2.6 4.4l-1.7-.8c-.6-.3-1 .6-1.6.1-.4-.5.6-1.1.2-1.8-.3-.6-.9-.5-1.1-.9z"/></svg>
      www.rkellowsurg.com
    </li>
  </ul>
</section>

<section class="card card-back">
  <h2 class="conditions-title">Conditions Treated</h2>
  <ul class="conditions">
    <li>Carpal Tunnel</li>
    <li>Trigger Finger</li>
    <li>Ganglion Cysts</li>
    <li>Hand Tumors</li>
    <li>Han &amp; Wrist Arthritis</li>
    <li>Hand, Wrist &amp; Elbow Tendonitis</li>
    <li>Fractures of the Hand, Wrist, Elbow and Humerus</li>
    <li>Nerve Injuries of the Hand, Wrist &amp; Elbow</li>
    <li>Microsurgery</li>
    <li>Wrist Arthroscopy</li>
    <li>Endoscopic Surgery</li>
  </ul>

  <div class="brand"><span class="brand-dot"></span>Kellow Hand</div>
</section>

</body>
</html>
```